The name of the company is Harbor Turns buying foreclosed homes and remodeling

A sleek classy card. It’s a home remodel and house flip company. Something mostly black with dark gray and red in color . Something with two f”s as a logo on front as shown in pictures. Kind of just let you guys run with it . I left a few pictures that should help
You guys get an idea of what I thought was good also left all the information for back of the card

Target Market(s)

Home remodel consumers

Industry/Entity Type

Construction Company

Contact Information for Business Card

All details are on photo

Font styles to use
Decorative

Colors

Designer to choose colors to be used in the design.

Requirements
Must have
• Name of company on front. Harbor Turns
Nice to have
• Up to you guys I trust you
Should not have
• Not sure

```html
<!DOCTYPE html>
<html lang="en">
<head>
<meta charset="utf-8">
<title>Harbor Turns – Business Card</title>
<link rel="stylesheet" href="https://fonts.googleapis.com/css2?family=Montserrat:wght@300;400;700&display=swap">
<style>
  :root {
    --backdrop: #efefef;
    --card: #232323;
    --ink: #ffffff;
    --ink-soft: #d6d6d6;
    --ink-muted: #a9a9a9;
    --accent: #a01f2c;
  }
  * { box-sizing: border-box; margin: 0; padding: 0; }
  html, body {
    width: 1200px; height: 1200px; overflow: hidden;
    background: var(--backdrop);
    font-family: "Montserrat", sans-serif;
  }
  .sheet {
    width: 1200px; height: 1200px;
    display: flex; flex-direction: column; align-items: center; justify-content: center;
    gap: 80px;
  }
  .card {
    position: relative;
    width: 760px; height: 434px;
    background: var(--card);
    border-radius: 26px;
    box-shadow: 0 10px 24px rgba(0,0,0,0.18);
    color: var(--ink);
  }
  /* Front */
  .card--front { display: flex; align-items: center; justify-content: center; }
  .brand {
    display: flex; align-items: center; gap: 16px;
  }
  .brand__mark {
    width: 18px; height: 18px; background: var(--ink-soft);
  }
  .brand__name {
    font-weight: 300; font-size: 30px; letter-spacing: 0.32em;
    text-transform: uppercase; color: var(--ink-soft);
  }
  /* Back */
  .identity {
    position: absolute; right: 460px; top: 168px;
    text-align: right; line-height: 1.15;
  }
  .identity__first { font-weight: 700; font-size: 28px; letter-spacing: 0.01em; }
  .identity__last { font-weight: 300; font-size: 28px; color: var(--ink-soft); }
  .divider {
    position: absolute; left: 318px; top: 122px;
    width: 2px; height: 150px; background: var(--accent);
  }
  .contacts {
    position: absolute; left: 345px; top: 128px;
    list-style: none; display: flex; flex-direction: column; gap: 14px;
  }
  .contacts__item {
    display: flex; align-items: center; gap: 14px;
    font-size: 17px; font-weight: 400; color: var(--ink);
  }
  .contacts__icon { width: 20px; height: 20px; flex: none; }
  .services {
    position: absolute; left: 0; right: 0; bottom: 44px;
    text-align: center; font-size: 15px; font-weight: 300;
    color: var(--ink-muted); letter-spacing: 0.01em;
  }
</style>
</head>
<body>
<main class="sheet">
  <section class="card card--front" aria-label="Card front">
    <div class="brand">
      <span class="brand__mark"></span>
      <span class="brand__name">Harbor Turns</span>
    </div>
  </section>

  <section class="card card--back" aria-label="Card back">
    <div class="identity">
      <p class="identity__first">DANIEL</p>
      <p class="identity__last">WHITAKER JR</p>
    </div>
    <span class="divider"></span>
    <ul class="contacts">
      <li class="contacts__item">
        <svg class="contacts__icon" viewBox="0 0 20 20" aria-hidden="true">
          <rect x="2" y="5" width="16" height="11" fill="#fff"/>
          <path d="M2 5 L10 11 L18 5" fill="none" stroke="#232323" stroke-width="1.4"/>
        </svg>
        dwhitakerjr@mailbox.com
      </li>
      <li class="contacts__item">
        <svg class="contacts__icon" viewBox="0 0 20 20" aria-hidden="true">
          <circle cx="10" cy="10" r="7" fill="#fff"/>
        </svg>
        @Harbor_Turns_
      </li>
      <li class="contacts__item">
        <svg class="contacts__icon" viewBox="0 0 20 20" aria-hidden="true">
          <circle cx="10" cy="10" r="7.5" fill="none" stroke="#fff" stroke-width="1.6"/>
          <ellipse cx="10" cy="10" rx="3.2" ry="7.5" fill="none" stroke="#fff" stroke-width="1.3"/>
          <path d="M2.5 10 H17.5 M4 6 H16 M4 14 H16" stroke="#fff" stroke-width="1.2"/>
        </svg>
        www.harborturns.com
      </li>
      <li class="contacts__item">
        <svg class="contacts__icon" viewBox="0 0 20 20" aria-hidden="true">
          <path d="M5 3 L8 3 L9 7 L7 8.5 C8 11 9.5 12.5 12 13.5 L13.5 11.5 L17 12.5 L17 16 C17 16.5 16.5 17 16 17 C9 17 3 11 3 4 C3 3.5 3.5 3 4 3 Z" fill="#fff"/>
        </svg>
        555-014-2290
      </li>
    </ul>
    <p class="services">General Contractor • Home Remodel • Concrete Alternatives</p>
  </section>
</main>
</body>
</html>
```